Whitmore Business Card Design

The name of the business is Dara Whitmore, CPA LLC
The service that we offer is Accounting, Tax & Consulting Services. I need it to have the following items:
Dara Whitmore, Principal
Phone Number
Email Address
Physical Address

I have attached the company logo, one in black and one in white. Please provide a design in black background and the other in white background. Please include "Accounting, Tax & Consulting Services". I want the business card to be clean and very professional.

```html
<!DOCTYPE html>
<html lang="en">
<head>
<meta charset="utf-8">
<title>Dara Whitmore, CPA LLC – Business Cards</title>
<link rel="stylesheet" href="https://fonts.googleapis.com/css2?family=Montserrat:wght@400;500;600;700&display=swap">
<style>
  :root {
    --backdrop: #d3d3d3;
    --card-light: #ffffff;
    --card-dark: #1d1d1f;
    --ink-dark: #3a3a3c;
    --ink-grey: #808080;
    --ink-light: #ffffff;
    --ink-soft: #b4b4b4;
    --accent-red: #97161c;
    --rule: #8a8a8a;
  }
  html, body {
    margin: 0;
    padding: 0;
    width: 1000px;
    height: 1200px;
    overflow: hidden;
    background: var(--backdrop);
    font-family: "Montserrat", Arial, sans-serif;
  }
  .canvas {
    position: relative;
    width: 1000px;
    height: 1200px;
  }
  .card {
    position: absolute;
    left: 134px;
    width: 732px;
    height: 419px;
  }
  .card--front { top: 159px; background: var(--card-light); }
  .card--back { top: 622px; background: var(--card-dark); }

  /* Front */
  .brand-block {
    position: absolute;
    left: 113px;
    top: 103px;
    width: 220px;
    height: 211px;
    display: flex;
    flex-direction: column;
    align-items: flex-start;
    justify-content: center;
    gap: 18px;
  }
  .brand-block__square {
    width: 46px;
    height: 46px;
    background: var(--accent-red);
  }
  .brand-block__name {
    font-weight: 600;
    font-size: 30px;
    line-height: 1.15;
    color: var(--ink-dark);
  }
  .divider {
    position: absolute;
    left: 365px;
    top: 101px;
    width: 2px;
    height: 213px;
    background: var(--rule);
  }
  .contact {
    position: absolute;
    left: 405px;
    top: 97px;
    color: var(--ink-grey);
  }
  .contact__name {
    margin: 0;
    font-weight: 700;
    font-size: 25px;
    color: var(--accent-red);
    line-height: 32px;
  }
  .contact__title {
    margin: 0;
    font-size: 18px;
    line-height: 26px;
  }
  .contact__address {
    margin: 24px 0 0;
    font-size: 18px;
    line-height: 25px;
    font-style: normal;
  }
  .contact__list {
    list-style: none;
    margin: 13px 0 0;
    padding: 0;
    font-size: 18px;
    line-height: 25px;
  }
  .contact__list li {
    display: flex;
    align-items: center;
    gap: 12px;
  }
  .contact__icon {
    width: 16px;
    height: 16px;
    fill: var(--accent-red);
    flex: none;
  }

  /* Back (dark version) */
  .lockup {
    position: absolute;
    inset: 0;
    display: flex;
    flex-direction: column;
    align-items: center;
    padding-top: 112px;
  }
  .lockup__square {
    width: 62px;
    height: 62px;
    background: var(--accent-red);
    margin-bottom: 42px;
  }
  .lockup__name {
    margin: 0;
    font-weight: 500;
    font-size: 30px;
    letter-spacing: 1px;
    text-transform: uppercase;
    color: var(--ink-light);
    line-height: 34px;
  }
  .lockup__tagline {
    margin: 4px 0 0;
    font-weight: 500;
    font-size: 21px;
    letter-spacing: 2.4px;
    text-transform: uppercase;
    color: var(--ink-soft);
    line-height: 28px;
  }
  .lockup__services {
    margin: 14px 0 0;
    font-weight: 400;
    font-size: 15px;
    letter-spacing: 1px;
    color: var(--ink-soft);
    line-height: 20px;
  }
</style>
</head>
<body>
<main class="canvas">
  <section class="card card--front" aria-label="Business card front, white">
    <div class="brand-block">
      <div class="brand-block__square"></div>
      <div class="brand-block__name">Dara<br>Whitmore</div>
    </div>
    <div class="divider"></div>
    <div class="contact">
      <h1 class="contact__name">Dara Whitmore</h1>
      <p class="contact__title">Principal</p>
      <address class="contact__address">4820 Alder Ridge Rd, Maple Falls<br>Minnesota(MN)</address>
      <ul class="contact__list">
        <li>
          <svg class="contact__icon" viewBox="0 0 16 16" aria-hidden="true"><path d="M3.2 1.5l2.4 2.6-1.3 1.8c.9 2 2.6 3.8 4.7 4.8l1.8-1.3 2.6 2.4-1.5 2.2C6.6 13.5 2.5 9.4 1 3z"/></svg>
          <span>1-800-555-0147</span>
        </li>
        <li>
          <svg class="contact__icon" viewBox="0 0 16 16" aria-hidden="true"><path d="M1 3.5h14v9H1z"/><path d="M1.6 4.2l6.4 4.8 6.4-4.8" fill="none" stroke="#fff" stroke-width="1"/></svg>
          <span>info@website.com</span>
        </li>
        <li>
          <svg class="contact__icon" viewBox="0 0 16 16" aria-hidden="true"><g fill="none" stroke="var(--accent-red)" stroke-width="1.3"><circle cx="8" cy="8" r="6.3"/><ellipse cx="8" cy="8" rx="2.8" ry="6.3"/><path d="M1.7 8h12.6M2.6 5h10.8M2.6 11h10.8"/></g></svg>
          <span>www.website.com</span>
        </li>
      </ul>
    </div>
  </section>

  <section class="card card--back" aria-label="Business card back, black">
    <div class="lockup">
      <div class="lockup__square"></div>
      <h2 class="lockup__name">Dara Whitmore, CPA, LLC</h2>
      <p class="lockup__tagline">Certified Public Accountant</p>
      <p class="lockup__services">Accounting, Tax &amp; Consulting Services</p>
    </div>
  </section>
</main>
</body>
</html>
```